Machine Sign

This is for a laundromat. I would like signs to hang above the machines from the ceiling indicating machine size. For example we have 6 loaders, 4 loaders, 2 loaders.

```html
<!DOCTYPE html>
<html lang="en">
<head>
<meta charset="utf-8">
<title>Machine Size Signs</title>
<link rel="stylesheet" href="https://fonts.googleapis.com/css2?family=Montserrat:wght@600;800&display=swap">
<style>
  :root {
    --backdrop: #f3e5bf;
    --sign-white: #ffffff;
    --peach: #f6bd85;
    --teal: #1a9693;
    --shadow: #a89a80;
  }
  * { margin: 0; padding: 0; box-sizing: border-box; }
  html, body {
    width: 1200px; height: 436px; overflow: hidden;
    background: var(--backdrop);
  }
  .sign-row { position: relative; width: 1200px; height: 436px; }
  .sign {
    position: absolute; top: 45px;
    width: 336px; height: 336px;
    background: var(--sign-white);
    box-shadow: 5px 5px 0 var(--shadow);
    overflow: hidden;
    font-family: "Montserrat", sans-serif;
    color: var(--teal);
  }
  .sign--six { left: 69px; }
  .sign--four { left: 432px; }
  .sign--two { left: 795px; }
  .sign__lower {
    position: absolute; left: 0; top: 164px;
    width: 100%; height: 172px;
    background: var(--peach);
  }
  .sign__arcs { position: absolute; left: 0; top: 0; width: 336px; height: 164px; }
  .brand {
    position: absolute; left: 0; top: 27px; width: 100%;
    display: flex; align-items: center; justify-content: center; gap: 8px;
  }
  .brand__dot {
    width: 38px; height: 38px; border-radius: 50%;
    background: var(--peach);
  }
  .brand__name {
    font-weight: 600; font-size: 24px; line-height: 1; color: var(--teal);
  }
  .sign__count {
    position: absolute; left: 0; top: 38px; width: 100%;
    text-align: center;
    font-weight: 800; font-size: 200px; line-height: 1;
  }
  .sign__label {
    position: absolute; left: 0; top: 218px; width: 100%;
    text-align: center;
    font-weight: 600; font-size: 38px; line-height: 1;
    letter-spacing: 0.12em; padding-left: 0.12em;
  }
  .sign__machine {
    position: absolute; left: 137px; top: 259px;
    width: 62px; height: 63px;
    background: linear-gradient(180deg, #e9b47f, #e3aa74);
    border-radius: 2px;
  }
</style>
</head>
<body>
<main class="sign-row">

  <section class="sign sign--six">
    <div class="sign__lower"></div>
    <svg class="sign__arcs" viewBox="0 0 336 164" aria-hidden="true">
      <circle cx="168" cy="169" r="83" fill="none" stroke="var(--teal)" stroke-width="1.5"/>
      <circle cx="168" cy="169" r="74" fill="none" stroke="var(--teal)" stroke-width="2.6"/>
    </svg>
    <div class="brand"><span class="brand__dot"></span><span class="brand__name">Sunny Suds</span></div>
    <div class="sign__count">6</div>
    <div class="sign__label">LOADERS</div>
    <div class="sign__machine" role="img" aria-label="Line icon of a front-loading washing machine"></div>
  </section>

  <section class="sign sign--four">
    <div class="sign__lower"></div>
    <svg class="sign__arcs" viewBox="0 0 336 164" aria-hidden="true">
      <circle cx="168" cy="169" r="83" fill="none" stroke="var(--teal)" stroke-width="1.5"/>
      <circle cx="168" cy="169" r="74" fill="none" stroke="var(--teal)" stroke-width="2.6"/>
    </svg>
    <div class="brand"><span class="brand__dot"></span><span class="brand__name">Sunny Suds</span></div>
    <div class="sign__count">4</div>
    <div class="sign__label">LOADERS</div>
    <div class="sign__machine" role="img" aria-label="Line icon of a front-loading washing machine"></div>
  </section>

  <section class="sign sign--two">
    <div class="sign__lower"></div>
    <svg class="sign__arcs" viewBox="0 0 336 164" aria-hidden="true">
      <circle cx="168" cy="169" r="83" fill="none" stroke="var(--teal)" stroke-width="1.5"/>
      <circle cx="168" cy="169" r="74" fill="none" stroke="var(--teal)" stroke-width="2.6"/>
    </svg>
    <div class="brand"><span class="brand__dot"></span><span class="brand__name">Sunny Suds</span></div>
    <div class="sign__count">2</div>
    <div class="sign__label">LOADERS</div>
    <div class="sign__machine" role="img" aria-label="Line icon of a front-loading washing machine"></div>
  </section>

</main>
</body>
</html>
```